Flyer für Wahlkampf
Zielgruppe
Ich benötige den Flyer für den Wahlkampf. Ich bin Kandidat für die Kommunalwahlen (Gemeinderats- und Kreistagswahl).
Aufgabenstellung
Der Flyer soll das Format DIN A5 haben und vier Seiten umfassen. Er soll einmal in der Mitte faltbar sein. Ob der Flyer in Hoch- oder Querformat erstellt wird, überlasse ich der Kreativität der Designer.
Die erste Seite soll das im Anhang beigefügte Bild von mir enthalten sowie die Angaben im beigefügten Word-Dokument. Idealerweise soll das Bild die ganze Seite einnehmen und die Angaben erscheinen an der Seite auf dem Bild. Ich überlasse dies jedoch der Kreativität der Designer.
Auf der zweiten Seite sollen die im Anhang beigefügten restlichen Bilder unter der Ruprik 'Meine bisherigen Erfolge für unsere Ortschaft:' erscheinen.
Der restliche Flyer soll dann nur aus Text bestehen, welcher kreativ angeordnet werden kann.
Allgemein habe ich hinsichtlich der Schriftart keine Vorstellungen und überlasse dies der Kreativität der Designer.
Dankeschön! :-)

```html
<!DOCTYPE html>
<html lang="de">
<head>
<meta charset="utf-8">
<title>Wahlflyer Lukas Brandt</title>
<link href="https://fonts.googleapis.com/css2?family=PT+Sans:wght@400;700&family=PT+Sans+Narrow:wght@400;700&family=Gochi+Hand&display=swap" rel="stylesheet">
<style>
:root{
  --navy:#2d2a6b;
  --ink:#222;
  --paper:#fff;
  --hand:#3b2fa0;
  --mark:#8a8a8a;
}
*{margin:0;padding:0;box-sizing:border-box}
html,body{width:1200px;height:424px;overflow:hidden;background:#fff}
body{position:relative;font-family:"PT Sans",sans-serif;color:var(--ink);font-size:6.1px;line-height:8.3px}
.panel{position:absolute;top:0;height:424px;overflow:hidden;background:var(--paper)}
.col{position:absolute}
h3{font-size:6.3px;font-weight:700;margin:4px 0 1px}
ul{list-style:none}
ul li::before{content:"• "}
p{margin:0}
.box-head{position:absolute;border:1.3px solid var(--navy);color:var(--navy);font-family:"PT Sans Narrow",sans-serif;font-size:9px;line-height:10.5px;padding:2px 5px;background:#fff}

/* panel 1 */
.p1{left:0;width:290px}
.letter{position:absolute;left:33px;top:258px;width:240px;font-family:"Gochi Hand",cursive;color:var(--hand);font-size:7px;line-height:9.3px}
.letter .greet{font-size:8px;margin-bottom:4px}
.letter p{margin-bottom:4px}
.letter .sign{margin-left:14px}

/* panel 2 */
.p2{left:292px;width:302px}
.portrait{position:absolute;left:0;top:0;width:302px;height:367px;background:radial-gradient(ellipse at 50% 45%,#6e6e6e 0%,#4d4d4d 70%,#3e3e3e 100%)}
.name-box{position:absolute;left:132px;top:12px;width:156px;height:29px;background:var(--navy);border:1.5px solid #fff;color:#fff;font-family:"PT Sans Narrow",sans-serif;font-size:17px;line-height:26px;text-align:center}
.party{position:absolute;right:14px;top:49px;color:#eee;font-size:5.6px}
.claim{position:absolute;left:68px;top:348px;width:234px;height:29px;background:var(--navy);color:#fff;font-family:"PT Sans Narrow",sans-serif;font-size:12px;line-height:29px;padding-left:10px}
.ballot{position:absolute;left:238px;top:318px;width:54px;height:54px;border-radius:50%;background:var(--mark)}
.election{position:absolute;left:160px;top:384px;width:130px;text-align:center}
.election .date{font-family:"PT Sans Narrow",sans-serif;font-size:9.5px;line-height:12px}
.election .lists{font-size:5.3px;line-height:6.6px}

/* panel 3 */
.p3{left:608px;width:308px}
.band{position:absolute;left:0;top:279px;width:308px;height:145px;background:var(--navy)}
.wheel{position:absolute;left:0;top:0}
.wheel-label{position:absolute;left:108px;top:290px;width:92px;text-align:center;color:var(--navy);font-family:"PT Sans Narrow",sans-serif;font-size:9px;line-height:10.5px}

/* panel 4 */
.p4{left:933px;width:267px}
.p4 p{margin-bottom:2px}
</style>
</head>
<body>

<section class="panel p1">
  <div class="col" style="left:23px;top:40px;width:120px">
    <p>anderer Kommunen zum Teil übersteigt. Dennoch werden die Aufgaben im Einsatzdienst für die Kameradinnen und Kameraden immer anspruchsvoller und vielschichtiger. Daher möchte ich mich auch weiterhin dafür stark machen, dass unsere Feuerwehren stets gut ausgestattet sind, denn die Sicherstellung des Brand- und Katastrophenschutzes zählt zu den wichtigsten Aufgaben der Gemeinde.</p>
    <h3>Keine Grundsteuererhöhung</h3>
    <p>Auch, wenn die dem Gesetzgeber vom Bundesverfassungsgericht aufgetragene Reform der Grundsteuer möglichst aufkommensneutral erfolgen soll, rechnet der Bund der Steuerzahler dennoch mit einer Erhöhung der Grundsteuerhebesätze durch die Kommunen. In Zeiten steigender Kosten kann eine weitere Belastung der Grundstückseigentümer in meinen Augen nicht angehen. Ich möchte mich im</p>
  </div>
  <div class="col" style="left:151px;top:40px;width:132px">
    <p>Gemeinderat dafür einsetzen, dass von einer Erhöhung des Hebesatzes Abstand genommen wird.</p>
    <h3>Weitere Ziele</h3>
    <ul>
      <li>Mehr Verkehrssicherheit</li>
      <li>Unterstützung der Gemeinde bei der Errichtung eines Jugend- und Freizeittreffs in Wiesenfeld</li>
      <li>Lösung der derzeit zwischen Gemeinde und dem Abwasserverband bestehenden Probleme</li>
      <li>Errichtung weiterer Blühwiesen</li>
      <li>Verschönerung des Ortsbildes durch Neupflanzungen</li>
      <li>eine funktionierende Kommunikation zwischen Einwohnerschaft und Gemeindeverwaltung</li>
    </ul>
    <h3>Sie haben weitere Anregungen oder Fragen? Kontaktieren Sie mich gern!</h3>
    <p>E-Mail: lukas.brandt@post-mail.de<br>Telefon: 0 176 - 12 34 56 78</p>
  </div>
  <div class="letter">
    <p class="greet">Liebe Einwohnerinnen und Einwohner,</p>
    <p>in den letzten 5 Jahren habe ich mich mit viel Herzblut für unsere Ortschaft und die Gemeinde eingesetzt, Themen und Probleme offen und transparent kommuniziert und mich Ihren Anliegen stets angenommen.</p>
    <p>Gern möchte ich diesen Kurs fortführen und bitte Sie daher zu den Kommunalwahlen am 09.06.2024 um Ihre drei Stimmen!</p>
    <p class="sign">Herzlichst,<br>Lukas Brandt</p>
  </div>
</section>

<section class="panel p2">
  <div class="portrait" role="img" aria-label="Porträtfoto des Kandidaten vor grauem Hintergrund"></div>
  <div class="name-box">Lukas Brandt</div>
  <div class="party">Freie Wählergemeinschaft (FWG)</div>
  <div class="claim">Ihr Kandidat für Wiesenfeld</div>
  <div class="ballot" role="img" aria-label="Gezeichnetes Wahlkreuz im Kreis"></div>
  <div class="election">
    <div class="date">Kommunalwahlen 09.06.2024</div>
    <div class="lists">Gemeinderat Lindenthal: Listenplatz 10<br>Kreistag Auenkreis: Listenplatz 9</div>
  </div>
</section>

<section class="panel p3">
  <div class="band"></div>
  <svg class="wheel" width="308" height="424" viewBox="0 0 308 424" role="img" aria-label="Kreis aus sechs Fotos: Friedhofskapelle, Tischtennisplatte, Schaukasten, Abfallbehälter und Wege">
    <defs>
      <linearGradient id="wheelTone" x1="0" y1="0" x2="1" y2="1">
        <stop offset="0" stop-color="#9fb07a"/>
        <stop offset="0.45" stop-color="#c9c9c4"/>
        <stop offset="1" stop-color="#6f7468"/>
      </linearGradient>
    </defs>
    <circle cx="154" cy="311" r="113" fill="url(#wheelTone)" stroke="#fff" stroke-width="3"/>
    <g stroke="#fff" stroke-width="3">
      <line x1="154" y1="311" x2="154" y2="198"/>
      <line x1="154" y1="311" x2="252" y2="255"/>
      <line x1="154" y1="311" x2="252" y2="367"/>
      <line x1="154" y1="311" x2="154" y2="424"/>
      <line x1="154" y1="311" x2="56" y2="367"/>
      <line x1="154" y1="311" x2="56" y2="255"/>
    </g>
    <polygon points="154,263 196,287 196,335 154,359 112,335 112,287" fill="#fff"/>
  </svg>
  <div class="wheel-label">Meine bisherigen Erfolge für unsere Ortschaft</div>

  <div class="box-head" style="left:18px;top:16px">Zu Meiner Person</div>
  <div class="box-head" style="left:167px;top:16px;width:104px">Meine bisherigen Erfolge für unsere Ortschaft</div>

  <ul class="col" style="left:17px;top:39px;width:136px">
    <li>27 Jahre alt</li>
    <li>Finanzbeamter</li>
    <li>wohnhaft in Wiesenfeld seit 1999, ich bin hier bereits zur Kita und in die damalige Grundschule gegangen</li>
    <li>Abitur in 2015 an der KGS „Am Lindenhof“ in Neustadt</li>
    <li>seit 04/2021: Studium der Rechtswissenschaften an der Fernuniversität Nord</li>
    <li>von 07/2019 bis 10/2023 Ortsbürgermeister der Ortschaft Wiesenfeld, seither Mitglied des Ortschaftsrates Wiesenfeld</li>
    <li>seit 12/2021: Mitglied des Gemeinderates Lindenthal</li>
    <li>Mitglied im TSV Blau-Weiß Wiesenfeld sowie im RSV Wiesenfeld</li>
  </ul>

  <ul class="col" style="left:169px;top:50px;width:136px">
    <li>Asphaltierung der Friedhofsstraße sowie weitere durchgeführte Tiefbaumaßnahmen</li>
    <li>Sanierung der Friedhofs-Trauerhalle</li>
    <li>flächendeckende Aufstellung von Abfallbehältern</li>
    <li>Errichtung eines Ortschaftsbüros</li>
    <li>Aufstellung neuer Schaukästen</li>
    <li>Aufstellung neuer Sitzbänke</li>
    <li>Anschaffung einer Tischtennisplatte für den Spielplatz</li>
    <li>Beschaffung eines neuen Einsatzfahrzeuges für die Freiwillige Feuerwehr</li>
    <li>Aufstellung einer neuen Feuerwehr-Einsatzsirene</li>
    <li>Unterstützung der Sportvereine beim Einbau einer neuen Heizungsanlage in die Wiesenfelder Turnhalle</li>
    <li style="padding-left:16px">Errichtung einer Blühwiese in der Hauptstraße</li>
    <li style="padding-left:42px">Ideengebung für neue Veranstaltungen (z.B. Ostermarkt, Weihnachtsmarkt)</li>
    <li style="padding-left:62px">und weitere kleinere Projekte</li>
  </ul>
</section>

<section class="panel p4">
  <div class="box-head" style="left:4px;top:16px">Was ich gerne noch bewirken möchte</div>
  <div class="col" style="left:0;top:40px;width:125px">
    <h3>Mehr Geld für Tiefbaumaßnahmen</h3>
    <p>In den letzten Jahren lag der finanzielle Fokus des Gemeinderates auf Investitionen in die sozialen Bereiche – was ich auch sehr begrüße. Dennoch befinden sich einige Straßen und vor allem viele Fußwege in unserer Ortschaft in keinem guten Zustand. Auch in Sachen Barrierefreiheit besteht erheblicher Nachholbedarf. Daher möchte ich mich dafür einsetzen, dass zukünftig mehr Geld für Tiefbaumaßnahmen im Haushalt zur Verfügung steht und dieses entsprechend der bereits aufgestellten Prioritätenliste auch eingesetzt wird.</p>
    <h3>Sanierung der Turnhalle</h3>
    <p>Unsere Sportvereine tragen einen bedeutenden Teil zum kulturellen Leben in unserer Ortschaft bei. Leider befindet sich die Wiesenfelder Turnhalle mittlerweile in keinem ansehnlichen und teilweise sogar in einem sanierungsbedürftigen Zustand. Ich möchte mich daher weiterhin für Investitionen in unsere Sportstätte stark machen. Insbesondere die Akquirierung von geeigneten Fördermitteln muss weiter vorangetrieben werden.</p>
    <h3>Schaffung einer kleinen Einkaufsgelegenheit</h3>
    <p>Ein Thema, das viele Einwohner bewegt, sind fehlende Einkaufsmöglichkeiten im Dorf. Die gesetzlichen Hürden für die Errichtung eines Supermarktes in unserer Ortschaft sind leider sehr hoch. Es gibt jedoch eine Menge alternative Konzepte für kleinere Einkaufsgelegenheiten, mit denen der Einwohnerschaft zumindest die Dinge des täglichen Grundbedarfes zur Verfügung gestellt werden könnten. Hierzu hatte ich zuletzt Gespräche mit Investoren,</p>
  </div>
  <div class="col" style="left:131px;top:40px;width:127px">
    <p>die Interesse bekundeten, unsere Ortschaft entsprechend zu versorgen. Aus diesem Grund möchte ich das Projekt gerne weiterverfolgen und vorantreiben.</p>
    <h3>Errichtung eines neuen Spielplatzes</h3>
    <p>Schon zum Heimatfest 2019 kamen viele Einwohnerinnen und Einwohner auf mich zu und äußerten den Wunsch nach einem Spielplatz in der Ortsmitte. In den letzten Jahren habe ich hierfür mit der Gemeindeverwaltung entsprechende Konzepte entwickelt, welche bisher noch nicht umgesetzt werden konnten. In der neuen Legislaturperiode möchte ich passende Fördermittel und Zuschüsse beschaffen und das Projekt nunmehr endlich realisieren.</p>
    <h3>Neue Rad- und Gehwege</h3>
    <p>Viele Einwohner wünschen sich die Errichtung von Rad- und Gehwegen in Richtung B 80 bzw. nach Neustadt. Das Sicherheitsgefühl würde sich dadurch für viele Verkehrsteilnehmer erhöhen. Es ist wichtig, hinsichtlich dieses Themas nichts zu beschönigen: Ohne Fördermittel wird die Gemeinde aufgrund der erheblichen Kosten nie dazu in der Lage sein, derartige Projekte zu realisieren. Dies bedeutet jedoch nicht, dass man hiervon gänzlich Abstand nehmen muss. Mein Bestreben ist, gezielte Planungen voranzutreiben und dass Wiesenfeld eine höhere Priorisierung im Radverkehrskonzept des Landkreises erhält. Somit steigen auch die Chancen auf Fördermittel.</p>
    <h3>Unterstützung der Freiwilligen Feuerwehren</h3>
    <p>Unsere Gemeindefeuerwehr wurde in den letzten Jahren mit modernster Technik ausgestattet, die sogar die Verhältnisse</p>
  </div>
</section>

</body>
</html>
```